Wild Ridge Trekcraft DL flyer

I'm looking for a new flyer for my startup business. In Darwin Australia.
Aimed at family's and short stay tourists the "Wild Ridge Trekcraft" 4 hr tour will give people a basic understanding of some essential bush survival skills in the Australian Outback.
things covered in this 4 hr tour are
1. Finding water.
2. finding food.
3. Finding/making shelter and fire.
4. Finding your way home.

The tour will pick clients up in an air conditioned purpose build 4WD and take them to a nearby bushland area where they will have the opportunity to catch and harvest some native bushtucker.
They will then be able to find/harvest some water for survival situations.
While we cook our bush tucker they will also learn to find their way home through ancient navigation techniques as well.

Clients will then be dropped back to their accomodation with some fun and vital knowledge of surviving in the Australian outback.
At the end of the tour the group will be able to take home a basic survival kit which they will be able to use through the skills they just gained on the tour.

I'd like a two sided DL size flyer emphasising the following points.
4hr/half day tour
Fun for the family
Free survival kit included.
Eat what you catch
Learn essential survival skills
Provided buy an experienced and passionate bushman.
$150/head including transfers.

I'll provide some pictures for the flyer and any extra content you require.
Updates

Target Market(s)

Family's
Short stay tourists

Industry/Entity Type

Tourism

Colors

Designer to choose colors to be used in the design.

Requirements
Must have
• As per brief
Nice to have
• Any extra content and flair designers would like to add
Should not have
• Any images which aren't Australian

```html
<!DOCTYPE html>
<html lang="en">
<head>
<meta charset="utf-8">
<title>Wild Ridge Trekcraft – DL Flyer</title>
<link rel="stylesheet" href="https://fonts.googleapis.com/css2?family=Graduate&family=Open+Sans:ital,wght@1,400;1,600&display=swap">
<style>
  :root{
    --backdrop:#e9e6e1;
    --wood-light:#e39a4f;
    --wood-mid:#c9772f;
    --wood-dark:#9c5420;
    --plank-line:rgba(90,45,12,.35);
    --frame:#ffffff;
    --ink-light:#ffffff;
  }
  *{box-sizing:border-box;margin:0;padding:0}
  html,body{width:1200px;height:1123px;overflow:hidden;background:var(--backdrop)}
  .canvas{position:relative;width:1200px;height:1123px}
  .flyer{
    position:absolute;top:103px;width:424px;height:918px;overflow:hidden;
    background:
      repeating-linear-gradient(90deg,transparent 0 40px,var(--plank-line) 40px 41px,transparent 41px 42px),
      radial-gradient(ellipse at 50% 45%,var(--wood-light) 0%,var(--wood-mid) 60%,var(--wood-dark) 100%);
    box-shadow:0 6px 14px rgba(0,0,0,.35);
  }
  .flyer--front{left:81px}
  .flyer--back{left:655px}
  .flyer__title{
    position:absolute;font-family:"Graduate",serif;color:var(--ink-light);
    font-size:42px;line-height:1.05;letter-spacing:1px;font-weight:400;
    text-shadow:2px 3px 4px rgba(0,0,0,.45);white-space:nowrap;
  }
  .flyer--front .flyer__title{left:22px;top:42px;transform:rotate(-8deg);transform-origin:left top}
  .flyer--back .flyer__title{right:16px;top:24px;text-align:right;transform:rotate(7deg);transform-origin:center}
  .photo{
    position:absolute;background:var(--frame);padding:7px;
    box-shadow:2px 4px 8px rgba(0,0,0,.4);
  }
  .photo__image{position:relative;width:100%;height:100%;overflow:hidden}
  .photo__caption{
    position:absolute;font-family:"Open Sans",sans-serif;font-style:italic;font-weight:400;
    color:var(--ink-light);font-size:21px;text-shadow:1px 1px 3px rgba(0,0,0,.7);white-space:nowrap;
  }
  .photo__label{
    position:absolute;font-family:"Open Sans",sans-serif;font-weight:600;font-style:italic;
    color:var(--ink-light);font-size:24px;text-shadow:1px 1px 3px rgba(0,0,0,.6);
  }
  .img--savanna{background:linear-gradient(180deg,#6f8f5a 0%,#4f7236 45%,#8a5a34 62%,#5e8a2e 100%)}
  .img--crayfish{background:radial-gradient(ellipse at 55% 45%,#6d8a6a 0%,#b88a78 45%,#6a4a32 100%)}
  .img--still{background:linear-gradient(160deg,#2f4a25 0%,#c9d6d8 40%,#5f9a3a 75%,#4f8a2c 100%)}
  .img--bushfood{background:radial-gradient(ellipse at 50% 55%,#7fa04a 0%,#d7b5a2 55%,#b89688 100%)}
  .img--pandanus{background:linear-gradient(160deg,#7c8a5a 0%,#3f6a2a 45%,#9a8e72 100%)}
  .img--ground{background:linear-gradient(170deg,#8d7a52 0%,#6f5e3c 60%,#a08c6a 100%)}
  .flyer__note{
    position:absolute;top:884px;font-family:"Open Sans",sans-serif;font-style:italic;color:var(--ink-light);
    font-size:19px;letter-spacing:1px;text-shadow:1px 1px 2px rgba(0,0,0,.4);white-space:nowrap;
  }
  .flyer__credit{
    position:absolute;left:114px;top:785px;width:280px;font-family:"Open Sans",sans-serif;font-style:italic;
    color:var(--ink-light);font-size:17px;line-height:1.35;text-align:center;
    transform:rotate(-10deg);transform-origin:center;text-shadow:1px 1px 2px rgba(0,0,0,.35);
  }

  .photo--savanna{left:9px;top:128px;width:373px;height:259px;transform:rotate(-7.7deg);z-index:3}
  .photo--crayfish{left:3px;top:388px;width:410px;height:210px;transform:rotate(-2deg);z-index:2}
  .photo--still{left:-8px;top:615px;width:400px;height:240px;transform:rotate(8deg);z-index:4}
  .photo--bushfood{left:59px;top:115px;width:350px;height:200px;transform:rotate(8deg);z-index:1}
  .photo--pandanus{left:25px;top:312px;width:395px;height:217px;transform:rotate(-1deg);z-index:2}
  .photo--ground{left:22px;top:499px;width:380px;height:262px;transform:rotate(-10deg);z-index:3}
</style>
</head>
<body>
<main class="canvas">

  <section class="flyer flyer--front" aria-label="Flyer front">
    <h1 class="flyer__title">WILD RIDGE<br>TREKCRAFT</h1>

    <figure class="photo photo--savanna">
      <div class="photo__image img--savanna" role="img" aria-label="Outback savanna woodland with termite mounds in long grass">
        <figcaption class="photo__caption" style="left:14px;bottom:12px;transform:rotate(-4deg);transform-origin:left bottom">4hr/half day tour</figcaption>
      </div>
    </figure>

    <figure class="photo photo--crayfish">
      <div class="photo__image img--crayfish" role="img" aria-label="Freshwater crayfish held in open hands">
        <figcaption class="photo__caption" style="left:14px;bottom:18px">Eat what you catch</figcaption>
      </div>
    </figure>

    <figure class="photo photo--still">
      <div class="photo__image img--still" role="img" aria-label="Plastic bag tied over leafy branch collecting water on grass">
        <figcaption class="photo__caption" style="left:10px;bottom:22px;transform:rotate(3deg);transform-origin:left bottom">Learn essential survival skills</figcaption>
      </div>
    </figure>

    <p class="flyer__note" style="left:16px">Free survival kit included</p>
  </section>

  <section class="flyer flyer--back" aria-label="Flyer back">
    <h2 class="flyer__title">WILD RIDGE<br>TREKCRAFT</h2>

    <figure class="photo photo--bushfood">
      <div class="photo__image img--bushfood" role="img" aria-label="Hand holding small green native bush fruits">
        <figcaption class="photo__caption" style="left:40px;top:6px;transform:rotate(2deg)">Finding food</figcaption>
      </div>
    </figure>

    <figure class="photo photo--pandanus">
      <div class="photo__image img--pandanus" role="img" aria-label="Pandanus palm fronds with fruit cluster">
        <figcaption class="photo__caption" style="left:10px;top:10px">Fun for the family</figcaption>
      </div>
    </figure>

    <figure class="photo photo--ground">
      <div class="photo__image img--ground" role="img" aria-label="Stick and stone shadow marks on dirt showing east and west">
        <figcaption class="photo__caption" style="left:16px;top:20px">Finding your way home</figcaption>
        <span class="photo__label" style="right:36px;top:50px">WEST</span>
        <span class="photo__label" style="left:100px;bottom:30px">EAST</span>
      </div>
    </figure>

    <p class="flyer__credit">Provided buy an experienced<br>and passionate bushman</p>

    <p class="flyer__note" style="left:53px">$150/head including transfers.</p>
  </section>

</main>
</body>
</html>
```